Commercial janitorial cleaning

Janitorial cleaning particularly for commercial buildings. Website needs to specify free estimates. Location of service is Hudson, Valatie, East Greenbush, Troy, Albany ny area. Services page with Janitorial services- General Office Cleaning, Construction Cleaning, Carpet Extraction, Consultation/Business, Lighting Maintenance, Seasonal Deep Cleaning, Window cleaning, Event Cleaning, Floor and Carpet Cleaning, Floor Striping and Waxing. Contact us page with email phone number on page and a request page that emails me if they have any questions. About us page-the picture of my family on it with a section I can type a story myself.

Target Market(s)

Commercial businesses

Industry/Entity Type

Janitorial Service

Number of Pages Required

4 page

Font styles to use
Serif
Sans Serif
Script

Colors
ec1f27
1b1b1b
ffffff
9d9d9d

Requirements
Must have
• Phone number 555-314-2760. Must have free estimates on home page. Going for industrial / modern look to website
Nice to have
• Logo is a red and black building so if those colors could be coordinated to website that would be awesome.

```html
<!DOCTYPE html>
<html lang="en">
<head>
<meta charset="utf-8">
<title>Brightline Cleaning Services</title>
<link rel="stylesheet" href="https://fonts.googleapis.com/css2?family=Raleway:wght@300;500;600&family=Oswald:wght@400;500&family=Open+Sans:wght@400;600&family=Source+Sans+3:ital,wght@0,400;0,600;1,400;1,600&display=swap">
<style>
:root{
  --red:#ec1f27;
  --red-soft:#f0555a;
  --ink:#1b1b1b;
  --white:#ffffff;
  --grey:#9d9d9d;
  --text:#555555;
  --line:#dddddd;
}
*{margin:0;padding:0;box-sizing:border-box}
html,body{width:1200px;height:2597px;overflow:hidden;background:var(--white)}
body{position:relative;font-family:"Open Sans",sans-serif;color:var(--text)}
.abs{position:absolute}

/* hero */
.hero{left:0;top:0;width:1200px;height:561px;background:linear-gradient(160deg,#4a4a4a 0%,#2a2a2a 45%,#151515 100%)}
.brand{left:173px;top:30px;display:flex;align-items:center;gap:10px;font-family:"Oswald",sans-serif;font-weight:500;font-size:22px;color:var(--red);letter-spacing:.5px}
.brand i{width:20px;height:20px;background:var(--red);display:block}
.callbar{left:632px;top:0;width:216px;height:52px;background:#a9a9a9;clip-path:polygon(18px 0,100% 0,100% 100%,0 100%);display:flex;align-items:center;gap:10px;padding-left:34px;color:var(--white);font-family:"Oswald",sans-serif}
.callbar small{display:block;font-size:11px;line-height:1}
.callbar b{display:block;font-size:21px;font-weight:400;line-height:1.1}
.quote-btn{left:831px;top:0;width:205px;height:52px;background:var(--red);clip-path:polygon(18px 0,100% 0,calc(100% - 14px) 100%,0 100%);color:var(--white);font-family:"Oswald",sans-serif;font-size:23px;display:flex;align-items:center;justify-content:center}
.nav{left:658px;top:64px;display:flex;gap:36px;font-family:"Open Sans",sans-serif;font-weight:600;font-size:15px;color:var(--white)}
.hero-title{left:0;width:1200px;top:232px;text-align:center;color:var(--white);font-family:"Raleway",sans-serif}
.hero-title .pre{font-weight:300;font-size:30px;line-height:1.1}
.hero-title h1{font-weight:500;font-size:46px;line-height:1.15}
.loc-label{left:0;width:1200px;top:476px;text-align:center;font-family:"Oswald",sans-serif;font-size:15px;color:var(--white)}
.loc-list{left:0;width:1200px;top:514px;display:flex;justify-content:center;gap:38px;font-family:"Oswald",sans-serif;font-size:20px;color:var(--white);padding-right:10px}

/* section heads */
.head{left:0;width:1200px;text-align:center;font-family:"Raleway",sans-serif}
.head small{display:block;font-size:15px;color:#777;letter-spacing:.5px}
.head h2{font-weight:500;color:var(--red);line-height:1.15}
.rule{height:2px;background:var(--line)}

.dots{left:1040px;top:590px;display:flex;flex-direction:column;gap:4px}
.dots span{width:34px;height:34px;border-radius:50%;display:block}

/* about */
.about-frame{left:173px;top:707px;width:343px;height:353px;background:var(--red)}
.about-photo{left:196px;top:729px;width:343px;height:355px;background:linear-gradient(160deg,#6d8a52,#9c6f5a 55%,#48506a)}
.about-copy{left:573px;top:740px;width:468px;font-size:12.5px;line-height:1.68;color:var(--text)}
.about-copy p+p{margin-top:19px}
.btn-grey{background:var(--grey);color:var(--white);font-size:11px;display:flex;align-items:center;justify-content:center;letter-spacing:.3px}

/* services */
.service{top:1219px;width:291px;height:194px;clip-path:polygon(12px 0,100% 0,calc(100% - 12px) 100%,0 100%)}
.service .pic{position:absolute;inset:0}
.service .cap{position:absolute;left:0;right:0;bottom:0;height:36px;background:var(--ink);color:var(--white);font-family:"Raleway",sans-serif;font-size:19px;display:flex;align-items:center;justify-content:center}

/* why */
.why{left:0;top:1521px;width:963px;height:265px;background:var(--red)}
.why-title{left:60px;width:295px;top:1550px;text-align:right;font-family:"Raleway",sans-serif;font-weight:600;font-size:27px;line-height:1.02;color:var(--white)}
.feature{width:271px;height:113px;background:var(--red-soft);color:var(--white);padding:14px 14px 0 61px}
.feature svg{position:absolute;left:16px;top:27px}
.feature h3{font-family:"Oswald",sans-serif;font-weight:400;font-size:14px;letter-spacing:.2px}
.feature p{font-size:10.5px;line-height:1.72;margin-top:10px}

/* testimonials */
.subline{left:0;width:1200px;top:1908px;text-align:center;font-family:"Source Sans 3",sans-serif;font-style:italic;font-weight:600;font-size:14px;line-height:1.4;color:var(--ink)}
.qmark{font-family:Georgia,serif;font-size:64px;color:#555;line-height:1}
.quote-text{left:220px;top:2004px;width:320px;text-align:center;font-family:"Source Sans 3",sans-serif;font-style:italic;font-size:18px;line-height:1.5;color:#555}
.avatar{left:272px;top:2142px;width:69px;height:69px;border-radius:50%;background:linear-gradient(#d9dce0,#8b9099)}
.person{left:355px;top:2158px;font-family:"Open Sans",sans-serif}
.person b{display:block;font-weight:600;font-size:18px;color:var(--ink)}
.person span{font-size:11px;color:#888}
.video{left:611px;top:1988px;width:416px;height:231px;border:3px solid var(--ink);border-radius:5px;background:linear-gradient(120deg,#cfd3d8,#eef0f2 60%,#b9bec5)}

/* footer */
.footer{left:0;top:2281px;width:1200px;height:316px;background:var(--ink)}
.strip-grey{left:204px;top:2283px;width:593px;height:50px;background:#a9a9a9;clip-path:polygon(18px 0,100% 0,calc(100% - 18px) 100%,0 100%)}
.strip-item{top:2287px;display:flex;align-items:center;gap:10px;font-family:"Oswald",sans-serif;color:var(--white)}
.strip-item small{display:block;font-size:11px;line-height:1}
.strip-item b{display:block;font-weight:400;font-size:20px;line-height:1.15}
.strip-divider{left:395px;top:2283px;width:20px;height:50px;background:var(--ink);clip-path:polygon(60% 0,100% 0,40% 100%,0 100%)}
.strip-red{left:785px;top:2283px;width:207px;height:50px;background:var(--red);clip-path:polygon(16px 0,100% 0,calc(100% - 16px) 100%,0 100%);color:var(--white);font-family:"Oswald",sans-serif;font-size:22px;display:flex;align-items:center;justify-content:center}
.foot-brand{left:0;width:1200px;top:2368px;display:flex;justify-content:center;align-items:center;gap:9px;font-family:"Oswald",sans-serif;font-weight:500;font-size:20px;color:var(--red)}
.foot-brand i{width:18px;height:18px;background:var(--red);display:block}
.col-title{top:2429px;font-family:"Open Sans",sans-serif;font-weight:600;font-size:12px;color:var(--white);text-align:center}
.foot-address{left:172px;width:200px;top:2450px;text-align:center;font-size:11px;line-height:1.6;color:#aaa}
.foot-locs{left:401px;width:400px;top:2460px;display:flex;justify-content:space-between;font-family:"Oswald",sans-serif;font-size:15px;color:#aaa}
.socials{left:860px;top:2459px;display:flex;gap:16px}
.socials span{width:22px;height:22px;border:2px solid #777;border-radius:50%;display:block}
.foot-rule{left:180px;top:2508px;width:850px;height:1px;background:#333}
.foot-nav{left:0;width:1200px;top:2529px;display:flex;justify-content:center;gap:24px;font-size:11px;color:#aaa}
.copyright{left:0;width:1200px;top:2560px;text-align:center;font-size:11px;color:#aaa}
</style>
</head>
<body>

<!-- hero -->
<header class="abs hero" role="img" aria-label="Dark photograph of a tall glass office building"></header>
<div class="abs brand"><i></i>BRIGHTLINE</div>
<div class="abs callbar">
  <svg width="22" height="22" viewBox="0 0 24 24"><path fill="#fff" d="M6.6 10.8a15 15 0 0 0 6.6 6.6l2.2-2.2a1 1 0 0 1 1-.25 11.4 11.4 0 0 0 3.6.57 1 1 0 0 1 1 1V20a1 1 0 0 1-1 1A17 17 0 0 1 3 4a1 1 0 0 1 1-1h3.5a1 1 0 0 1 1 1c0 1.25.2 2.45.57 3.6a1 1 0 0 1-.25 1z"/></svg>
  <div><small>CALL US</small><b>555-314-2760</b></div>
</div>
<div class="abs quote-btn">GET A FREE QUOTE</div>
<nav class="abs nav"><span>Home</span><span>About Us</span><span>Services</span><span>Contact Us</span></nav>
<div class="abs hero-title">
  <div class="pre">Janitorial Cleaning Particularly for</div>
  <h1>Commercial Buildings</h1>
</div>
<div class="abs loc-label">LOCATION OF SERVICE</div>
<div class="abs loc-list"><span>HUDSON</span><span>VALATIE</span><span>EAST GREENBUSH</span><span>TROY</span><span>ALBANY</span></div>

<!-- welcome -->
<div class="abs head" style="top:600px">
  <small>WELCOME TO</small>
  <h2 style="font-size:35px">Brightline Cleaning Services</h2>
</div>
<div class="abs rule" style="left:346px;top:666px;width:508px"></div>
<div class="abs dots">
  <span style="background:var(--red)"></span>
  <span style="background:var(--ink)"></span>
  <span style="background:var(--grey)"></span>
</div>

<div class="abs about-frame"></div>
<div class="abs about-photo" role="img" aria-label="Family photo of the owners with their baby on a ladder in a garden"></div>
<div class="abs about-copy">
  <p>Lorem ipsum dolor sit amet, consectetur adipiscing elit, sed do eiusmod tempor incididunt ut labore et dolore magna aliqua. Ut enim ad minim veniam, quis nostrud exercitation ullamco laboris nisi ut aliquip ex ea commodo consequat. Duis aute irure dolor in reprehenderit in voluptate velit esse cillum dolore eu fugiat nulla pariatur. Excepteur sint occaecat cupidatat non proident, sunt in culpa qui officia deserunt mollit anim id est laborum.</p>
  <p>Sed ut perspiciatis unde omnis iste natus error sit voluptatem accusantium doloremque laudantium, totam rem aperiam, eaque ipsa quae ab illo inventore veritatis et quasi architecto beatae vitae dicta sunt explicabo. Nemo enim ipsam voluptatem quia voluptas sit aspernatur aut odit aut fugit, sed quia consequuntur magni dolores eos qui ratione voluptatem sequi nesciunt. Neque porro quisquam est, qui dolorem ipsum quia dolor sit amet, consectetur, adipisci velit.</p>
</div>
<div class="abs btn-grey" style="left:539px;top:1048px;width:128px;height:35px">READ MORE</div>

<!-- services -->
<div class="abs head" style="top:1126px">
  <small>OUR SERVICES</small>
  <h2 style="font-size:27px">What We Do</h2>
</div>
<div class="abs rule" style="left:452px;top:1186px;width:296px"></div>

<div class="abs service" style="left:173px">
  <div class="pic" role="img" aria-label="Yellow mop bucket and wet floor sign" style="background:linear-gradient(135deg,#5f6b7a,#c9b23a 55%,#3c3f44)"></div>
  <div class="cap">Janitorial Services</div>
</div>
<div class="abs service" style="left:454px">
  <div class="pic" role="img" aria-label="Cleaners working in an office" style="background:linear-gradient(135deg,#9fb3c2,#dfe6ea 50%,#4b5560)"></div>
  <div class="cap">General Office Cleaning</div>
</div>
<div class="abs service" style="left:736px">
  <div class="pic" role="img" aria-label="Worker cleaning a construction floor" style="background:linear-gradient(135deg,#c8cbcc,#9a9d9f 55%,#c76a2a)"></div>
  <div class="cap">Construction Cleaning</div>
</div>
<div class="abs btn-grey" style="left:535px;top:1437px;width:130px;height:37px">VIEW MORE</div>

<!-- why choose -->
<section class="abs why"></section>
<div class="abs why-title">Why Choose<br>Brightline<br>Cleaning Services</div>

<div class="abs feature" style="left:393px;top:1535px">
  <svg width="28" height="28" viewBox="0 0 28 28" fill="none" stroke="#fff" stroke-width="1.6"><circle cx="14" cy="14" r="5"/><circle cx="14" cy="14" r="11" stroke-dasharray="4 3"/></svg>
  <h3>QUALITY</h3>
  <p>Lorem ipsum dolor sit amet, conse ctetur adipiscing elit, sed do eiusmod tempor incididunt.</p>
</div>
<div class="abs feature" style="left:677px;top:1535px">
  <svg width="28" height="28" viewBox="0 0 28 28" fill="none" stroke="#fff" stroke-width="1.6"><circle cx="10" cy="17" r="6"/><circle cx="19" cy="9" r="5"/></svg>
  <h3>SERVICES</h3>
  <p>Lorem ipsum dolor sit amet, conse ctetur adipiscing elit, sed do eiusmod tempor incididunt.</p>
</div>
<div class="abs feature" style="left:393px;top:1661px">
  <svg width="28" height="28" viewBox="0 0 28 28" fill="none" stroke="#fff" stroke-width="1.6"><path d="M14 3l9 4v7c0 6-4 9-9 11-5-2-9-5-9-11V7z"/><path d="M10 14l3 3 5-6"/></svg>
  <h3>RESPONSIBLE AND TRUSTWORTHY</h3>
  <p>Lorem ipsum dolor sit amet, conse ctetur adipiscing elit, sed do eiusmod tempor incididunt.</p>
</div>
<div class="abs feature" style="left:677px;top:1661px">
  <svg width="28" height="28" viewBox="0 0 28 28" fill="none" stroke="#fff" stroke-width="1.6"><circle cx="14" cy="11" r="7"/><path d="M10 17l-2 9 6-3 6 3-2-9"/></svg>
  <h3>CERTIFIED GREEN COMPANY</h3>
  <p>Lorem ipsum dolor sit amet, conse ctetur adipiscing elit, sed do eiusmod tempor incididunt.</p>
</div>

<!-- testimonials -->
<div class="abs head" style="top:1830px">
  <small>TESTIMONIALS</small>
  <h2 style="font-size:27px"><svg width="24" height="24" viewBox="0 0 24 24" style="vertical-align:-3px;margin-right:10px"><circle cx="12" cy="12" r="12" fill="var(--red)"/><path fill="#fff" d="M7 15v-3c0-2 1-3 3-4v2c-1 0-1.5 1-1.5 2H10v3zm6 0v-3c0-2 1-3 3-4v2c-1 0-1.5 1-1.5 2H16v3z"/></svg>Happy Customers</h2>
</div>
<div class="abs rule" style="left:452px;top:1890px;width:296px"></div>
<div class="abs subline">Lorem ipsum dolor sit amet, consectetur adipiscing elit,<br>sed do eiusmod tempor</div>

<div class="abs qmark" style="left:178px;top:1985px">&ldquo;</div>
<div class="abs quote-text">&ldquo;Sed ut perspiciatis unde omnis iste natus error sit voluptatem accusantium doloremque laudantium, totam rem aperiam, eaque ipsa quae ab&rdquo;</div>
<div class="abs qmark" style="left:560px;top:2080px">&rdquo;</div>
<div class="abs avatar" role="img" aria-label="Customer portrait"></div>
<div class="abs person"><b>Jonanthan Doe</b><span>Lorem ipsum dolor</span></div>

<div class="abs video" role="img" aria-label="Video thumbnail of a cleaner mopping an office floor">
  <svg width="80" height="80" viewBox="0 0 80 80" style="position:absolute;left:165px;top:73px"><circle cx="40" cy="40" r="37" fill="rgba(0,0,0,.25)" stroke="#fff" stroke-width="3"/><path d="M32 25l24 15-24 15z" fill="#fff"/></svg>
</div>

<!-- footer -->
<footer class="abs footer"></footer>
<div class="abs strip-grey"></div>
<div class="abs strip-item" style="left:234px">
  <svg width="28" height="28" viewBox="0 0 24 24"><path fill="#fff" d="M6.6 10.8a15 15 0 0 0 6.6 6.6l2.2-2.2a1 1 0 0 1 1-.25 11.4 11.4 0 0 0 3.6.57 1 1 0 0 1 1 1V20a1 1 0 0 1-1 1A17 17 0 0 1 3 4a1 1 0 0 1 1-1h3.5a1 1 0 0 1 1 1c0 1.25.2 2.45.57 3.6a1 1 0 0 1-.25 1z"/></svg>
  <div><small>CALL US</small><b>555-314-2760</b></div>
</div>
<div class="abs strip-divider"></div>
<div class="abs strip-item" style="left:428px">
  <svg width="30" height="24" viewBox="0 0 30 24"><rect x="1" y="2" width="28" height="20" rx="2" fill="#fff"/><path d="M2 4l13 10 13-10" fill="none" stroke="#a9a9a9" stroke-width="2"/></svg>
  <div><small>EMAIL US</small><b>HELLO@BRIGHTLINECLEAN.EXAMPLE</b></div>
</div>
<div class="abs strip-red">GET A FREE QUOTE</div>

<div class="abs foot-brand"><i></i>BRIGHTLINE</div>

<div class="abs col-title" style="left:172px;width:200px">CONTACT US</div>
<div class="abs foot-address">Your Company LTD.<br>Street Name, 000000, City Name</div>
<div class="abs col-title" style="left:501px;width:200px">LOCATION OF SERVICE</div>
<div class="abs foot-locs"><span>HUDSON</span><span>VALATIE</span><span>EAST GREENBUSH</span><span>TROY</span><span>ALBANY</span></div>
<div class="abs col-title" style="left:830px;width:200px">GET CONNECTED</div>
<div class="abs socials"><span></span><span></span><span></span><span></span></div>

<div class="abs foot-rule"></div>
<nav class="abs foot-nav"><span>Home</span><span>About Us</span><span>Services</span><span>Contact Us</span></nav>
<div class="abs copyright">&copy; 2017 Brightline Cleaning Services. All Rights Reserved</div>

</body>
</html>
```